Marlow Hire IT Recruiting firm needs a business card design for Recruiters, Sourcers, and Account

We need business cards that allow us to change all contact info, names, titles (Recruiter, Sourcer, Account Manager, Director, CEO, etc) per person since we have three offices, in three cities, Phoenix, Austin, and Las Vegas. We do recruiting and contractors for IT positions (Developers, Architects, Software Engineers, Security Engineers, Help Desk, DBAs, PMs, Scrum Masters, etc.) Our client companies are very diverse from Meridex 100 to silicone Valley type start-ups.

So, while we what hip, techie, and quirky, it still needs to be professional. Primary color we use is blue, with silver as a secondary color.

Target Market(s)

IT, Technology

Industry/Entity Type

Business

Contact Information for Business Card

Company name: Marlow Hire, Inc.
Website: www.marlowhire-example.com
Logos for Workvine, Blurtly, and Gathra

Name, Title, Office Number, Cell Number, email

Font styles to use
Serif
Sans Serif

Colors
0455a3
d5d5d5

Requirements
Nice to have
• The grey I selected below is not necessary - but, would like silver included. I included a card design (File 3: MHI early trial example.jpg) that I had started on. It's very rough, and not quite what we're looking for, but what we did like is the logo, big, maybe a bit faded, off center, goes out of frame, etc. Still looking for other ideas - you are the pros! But, just an idea of a design element we liked.

```html
<!DOCTYPE html>
<html lang="en">
<head>
<meta charset="utf-8">
<title>Marlow Hire – Business Card</title>
<link href="https://fonts.googleapis.com/css2?family=Cinzel:wght@400&family=Lato:wght@400&family=Raleway:wght@300&display=swap" rel="stylesheet">
<style>
  :root {
    --page-bg: #e9e9ea;
    --card-bg: #0b0b0c;
    --card-glow: #141416;
    --brand-blue: #2f8fff;
    --brand-blue-deep: #0455a3;
    --silver: #d5d5d5;
    --silver-dim: #8d8d90;
    --text-light: #f1f1f1;
  }
  * { margin: 0; padding: 0; box-sizing: border-box; }
  html, body {
    width: 1200px; height: 900px; overflow: hidden;
    background: var(--page-bg);
  }
  .canvas {
    position: relative; width: 1200px; height: 900px;
    display: flex; align-items: center; justify-content: center; gap: 60px;
  }
  .card {
    position: relative; width: 520px; height: 297px;
    background: var(--card-bg); border-radius: 4px; overflow: hidden;
    box-shadow: 0 10px 30px rgba(0,0,0,0.25);
    font-family: "Lato", sans-serif;
  }
  .card__backdrop {
    position: absolute; width: 420px; height: 420px; border-radius: 50%;
    background: radial-gradient(circle, var(--card-glow) 0%, #101012 70%, transparent 71%);
  }
  .card--back .card__backdrop { left: 50px; top: -90px; }
  .card--front .card__backdrop { left: 150px; top: -40px; }

  /* back */
  .back__content {
    position: absolute; inset: 0; display: flex; flex-direction: column;
    align-items: center; padding-top: 78px;
  }
  .brand {
    display: flex; align-items: center; gap: 14px; height: 96px;
  }
  .brand__dot {
    width: 64px; height: 64px; border-radius: 50%;
    background: var(--brand-blue-deep);
  }
  .brand__name {
    font-family: "Cinzel", serif; font-size: 26px; color: var(--silver);
    letter-spacing: 1.5px; white-space: nowrap;
  }
  .back__url { margin-top: 14px; font-size: 15px; color: var(--silver); letter-spacing: 0.5px; }
  .social { display: flex; gap: 14px; margin-top: 12px; list-style: none; }
  .social__item { display: flex; align-items: center; gap: 5px; font-size: 10px; color: var(--silver); }
  .social__dot { width: 10px; height: 10px; border-radius: 50%; background: var(--silver); }

  /* front */
  .front__content {
    position: absolute; inset: 0; display: flex; flex-direction: column;
    align-items: center; padding-top: 44px;
  }
  .wordmark {
    font-family: "Cinzel", serif; font-weight: 400; font-size: 34px; color: var(--silver);
    letter-spacing: 2px; white-space: nowrap;
  }
  .tagline {
    margin-top: 6px; font-family: "Cinzel", serif; font-size: 11px;
    letter-spacing: 2.5px; color: var(--silver-dim); white-space: nowrap;
  }
  .person { margin-top: 14px; text-align: center; }
  .person__name { font-family: "Raleway", sans-serif; font-weight: 300; font-size: 23px; color: var(--text-light); }
  .person__title { font-size: 12px; color: var(--brand-blue); margin-top: 1px; }
  .contact { margin-top: 16px; font-size: 14px; line-height: 1.45; color: var(--silver); text-align: left; }
  .contact__label { color: var(--brand-blue); }
</style>
</head>
<body>
<main class="canvas">
  <section class="card card--back" aria-label="Card back">
    <div class="card__backdrop" role="img" aria-label="Faint large brand emblem backdrop"></div>
    <div class="back__content">
      <div class="brand">
        <span class="brand__dot"></span>
        <span class="brand__name">Marlow Hire</span>
      </div>
      <p class="back__url">www.marlowhire-example.com</p>
      <ul class="social">
        <li class="social__item"><span class="social__dot"></span>Gathra</li>
        <li class="social__item"><span class="social__dot"></span>Blurtly</li>
        <li class="social__item"><span class="social__dot"></span>Workvine</li>
      </ul>
    </div>
  </section>

  <section class="card card--front" aria-label="Card front">
    <div class="card__backdrop" role="img" aria-label="Faint large brand emblem backdrop"></div>
    <div class="front__content">
      <h1 class="wordmark">MARLOW HIRE</h1>
      <p class="tagline">HIRING TALENT THAT FITS</p>
      <div class="person">
        <p class="person__name">Dana Reyes K</p>
        <p class="person__title">Director</p>
      </div>
      <div class="contact">
        <p><span class="contact__label">T:</span> 555-0142-0187</p>
        <p><span class="contact__label">M:</span> 555-0142-0187</p>
        <p><span class="contact__label">E:</span> info@marlowhire-example.com</p>
      </div>
    </div>
  </section>
</main>
</body>
</html>
```